Communication Coach needs a business card

https://imgvaultcdn.example/design_img/3817205/61824/61824_27395018_3817205_8c2e7d1b_thumbnail.png

I like this a lot

I want it to include the following

Delia Fenwick
M.A.CCC-SLP
628-417-2093
delia.fenwick@quillpost.example
Communication Trainer and Executive Function Coaching
Be Confident-Be Authentic- Be Memorable

on back of card
Public Speaking
Executive Function Coaching
Interview Skills
Corporate Workshops
Self Regulation/Confidence Building

Target Market(s)

adults, parents

Contact Information for Business Card

See above description. i included picture of what i like

Requirements
Must have
• two sides, multi colors ,double sided
Nice to have
• I could have a tag line on front such as Be confident-Be memorable -Be authentic
Should not have
• not too busy or creative as needs to work for corporate setting

```html
<!DOCTYPE html>
<html lang="en">
<head>
<meta charset="utf-8">
<title>Delia Fenwick – Business Card</title>
<link rel="stylesheet" href="https://fonts.googleapis.com/css2?family=Poppins:wght@400;500;600;700&family=Allura&display=swap">
<style>
  :root {
    --bg: #d6d6d6;
    --purple: #8e56a2;
    --yellow: #f2d544;
    --pink: #ef5d72;
    --teal: #37b1a7;
    --green: #96c84c;
    --orange: #f07c58;
    --ink: #2b2b2b;
    --rule: #8a8a8a;
    --white: #ffffff;
  }
  * { box-sizing: border-box; margin: 0; padding: 0; }
  html, body { width: 1200px; height: 900px; overflow: hidden; }
  body {
    background: var(--bg);
    font-family: "Poppins", sans-serif;
    display: flex;
    flex-direction: column;
    align-items: center;
    justify-content: center;
    gap: 56px;
  }
  .card {
    width: 660px;
    height: 377px;
    border-radius: 24px;
    overflow: hidden;
    position: relative;
    background: var(--white);
  }

  /* Back side */
  .card-back { display: flex; }
  .service-band {
    flex: 1;
    display: flex;
    align-items: center;
    justify-content: center;
  }
  .service-band span {
    writing-mode: vertical-rl;
    transform: rotate(180deg);
    color: var(--white);
    font-weight: 500;
    font-size: 17px;
    letter-spacing: 0.5px;
    text-transform: uppercase;
    text-align: center;
    line-height: 1.25;
  }
  .band-purple { background: var(--purple); }
  .band-yellow { background: var(--yellow); }
  .band-pink { background: var(--pink); }
  .band-teal { background: var(--teal); }
  .band-green { background: var(--green); }
  .band-orange { background: var(--orange); }

  /* Front side */
  .color-strip {
    position: absolute;
    left: 0; right: 0;
    height: 44px;
    display: flex;
  }
  .color-strip div { flex: 1; }
  .strip-top { top: 0; }
  .strip-bottom { bottom: 0; }

  .front-content {
    position: absolute;
    top: 44px; bottom: 44px; left: 0; right: 0;
    display: flex;
    flex-direction: column;
    align-items: center;
    justify-content: center;
    color: var(--ink);
    text-align: center;
  }
  .headline {
    font-weight: 700;
    font-size: 22px;
    line-height: 1.15;
    letter-spacing: 0.5px;
    text-transform: uppercase;
  }
  .tagline {
    font-size: 15px;
    margin-top: 8px;
    letter-spacing: 0.3px;
  }
  .name-row {
    display: flex;
    align-items: center;
    width: 560px;
    margin-top: 2px;
    gap: 12px;
  }
  .name-row .rule {
    flex: 1;
    height: 1px;
    background: var(--rule);
  }
  .name {
    font-family: "Allura", cursive;
    font-size: 68px;
    line-height: 1.05;
    white-space: nowrap;
  }
  .credentials {
    align-self: flex-end;
    margin-right: 150px;
    margin-top: -8px;
    font-size: 14px;
    letter-spacing: 0.5px;
  }
  .contact {
    margin-top: 16px;
    font-size: 18px;
    letter-spacing: 0.3px;
  }
</style>
</head>
<body>

  <section class="card card-back" aria-label="Card back – services">
    <div class="service-band band-purple"></div>
    <div class="service-band band-yellow"><span>Public Speaking</span></div>
    <div class="service-band band-pink"><span>Executive Function<br>Coaching</span></div>
    <div class="service-band band-teal"><span>Interview Skills</span></div>
    <div class="service-band band-green"><span>Corporate Workshops</span></div>
    <div class="service-band band-orange"><span>Self Regulation/<br>Confidence Building</span></div>
  </section>

  <section class="card card-front" aria-label="Card front – contact">
    <div class="color-strip strip-top">
      <div class="band-purple"></div><div class="band-yellow"></div><div class="band-pink"></div>
      <div class="band-teal"></div><div class="band-green"></div><div class="band-orange"></div>
    </div>

    <div class="front-content">
      <h1 class="headline">Communication Trainer and Executive<br>Function Coaching</h1>
      <p class="tagline">Be Confident-Be Authentic- Be Memorable</p>
      <div class="name-row">
        <span class="rule"></span>
        <span class="name">Delia Fenwick</span>
        <span class="rule"></span>
      </div>
      <p class="credentials">M.A.CCC-SLP</p>
      <p class="contact">628-417-2093 | delia.fenwick@quillpost.example</p>
    </div>

    <div class="color-strip strip-bottom">
      <div class="band-purple"></div><div class="band-yellow"></div><div class="band-pink"></div>
      <div class="band-teal"></div><div class="band-green"></div><div class="band-orange"></div>
    </div>
  </section>

</body>
</html>
```